依頼詳細
表面はカラー、裏面は白黒で申し込み用紙にしようと考えています。
魅力のあるツアーだと思いますので、読み手に伝わるよう作成をお願いします。
〈ツアーのポイント〉
・透き通った青い海、緑の山々、満天の星空など、大自然に囲まれたダイナミックな眺望
・貸切バスで観光スポットをご案内
・地元の食材にこだわった料理を堪能
・島人との交流
・自然の中でBBQ、キャンプファイヤー
・宿泊は神津島唯一の温泉宿
・カップル成立で特典付き
・格安
など
多少変更が出るかもしれませんので、こちらでも編集できる形式で納品をお願いします。
ご不明点などありましたらご連絡ください。
よろしくお願いいたします。
記載項目
表現など変更して頂いて結構です。

【表面】
独身女性参加者募集
〈イベント名称〉渚トーク星結び
〈日時〉2015年7月3日(金)~2015年7月5日(日)
〈会場〉神津島
〈ツアースケジュール〉
1日目 20:00 東京 灯波客船ターミナル集合(女性のみ)・女子会
23:00 出航(大型客船)
2日目 9:00 神津島着・チェックイン
朝 男性合流・アイスブレイク
昼 昼食・島内観光
夜 BBQ・キャンプファイヤー・温泉旅館宿泊
3日目 朝 自由時間
13:35 神津島発
17:30 東京 灯波客船ターミナル着・解散
〈ツアーのポイント〉依頼詳細参考
〈集合場所〉白浪航路灯波港 1階ロビー ※若葉環状線蓮見坂駅から徒歩8分
〈集合時間〉2015年7月3日(金)20:00
〈参加対象〉20歳~35歳の島外在住独身女性
〈募集人数〉15名(先着順)
〈参加料金〉15,000円/1人(交通費・宿泊費・食費込み)
〈申込方法〉裏面の申込書にご記入の上、メール・FAX・郵送にてお申込みください。
〈申込締切〉2015年6月7日(日)
〈ホームページ〉
※ホームページのURLを載せたいのですが、まだ出来上がっていないので後ほどURLを追加できるようにしていただきたいです。

裏面は補足情報に記載します。
サイズ
A4
ページ数
両面
希望イメージ
• +5 0 +5
• シンプル
複雑
• 単色
カラフル
• 暗い
明るい
• 日常
高級
• 遊び心
厳粛
• 未来的
伝統的
• 女性的
男性的
希望する色
赤系、水色系、緑系、黄・オレンジ系
納品ファイル
補足説明
【裏面】申込用紙
〈イベント名称〉
〈日時〉
〈会場〉
〈募集人数〉15名(先着順)
〈参加資格〉20歳から35歳までの神津島外在住の独身女性
お一人様参加・シングルマザー・結婚歴あり歓迎
〈参加料金〉
MAIL  shiomi@hx.nagisanet-example.jp
メールでのお申し込みは①氏名②生年月日③住所④電話番号⑤メールアドレスを添えて上記のアドレスまでご送信ください。
FAX 04992-7-5530
〈申し込みフォーム〉
・氏名(ふりがな)
・氏名
・生年月日
・電話番号
・メールアドレス
・自己PR
〈注意事項〉
1 申し込み・キャンセルは6月7日(日)までにお願いします。
2 男女比は出来る限り調整しますが同数にならないこともありますのでご了承願います。
3 個人情報は厳重に管理し、本事業のみの使用とさせていただきます。
4 悪天候時はプログラム内容を変更または中止する場合があります。

申し込み受付後、事務局より順次詳細をお送りいたします。

問い合わせ・お申込み 汐見村商工会青年部事務局
〒100-0999 東京都汐見村汐見村2483番地
TEL  04992-7-4418
FAX  04992-7-5530

依頼公開後の追記内容
写真を添付します。

ターゲット層を対象にアンケート調査を実施した結果、最も多く票が集まったため。

この度は私どもの為に、多数ご提案をご用意していただき、誠にありがとうございます。どの提案も魅力を感じていましたが、上記の理由から一社選ばせていただきました。
折角親身にお世話をしていただいたところ、心苦しい限りですが、ご理解いただければ幸いです。
また、同様の機会があればよろしくお願いいたします。

```html
<!DOCTYPE html>
<html lang="ja">
<head>
<meta charset="utf-8">
<title>渚トーク星結び 参加申込用紙</title>
<link rel="stylesheet" href="https://fonts.googleapis.com/css2?family=Noto+Sans+JP:wght@400;500;700;900&display=swap">
<style>
  :root {
    --ink: #1a1a1a;
    --paper: #ffffff;
    --band: #2b2b2b;
    --mid: #6e6e6e;
    --soft: #d9d9d9;
    --tint: #f1f1f1;
  }
  * { margin: 0; padding: 0; box-sizing: border-box; }
  html, body { width: 847px; height: 1200px; overflow: hidden; background: var(--paper); }
  body { font-family: "Noto Sans JP", sans-serif; color: var(--ink); }
  .sheet { position: relative; width: 847px; height: 1200px; overflow: hidden; }

  .event-title {
    position: absolute; top: 30px; left: 0; width: 100%;
    display: flex; align-items: center; justify-content: center; gap: 18px;
    font-family: "Noto Sans JP", sans-serif; font-weight: 900;
    font-size: 72px; line-height: 1.2; letter-spacing: 4px; color: var(--ink);
  }
  .title-mark { width: 26px; height: 26px; border-radius: 50%; background: var(--ink); flex: none; }

  .form-heading {
    position: absolute; top: 130px; left: 190px; width: 467px;
    border-top: 2px solid var(--ink); border-bottom: 2px solid var(--ink);
    text-align: center; font-size: 34px; font-weight: 700; letter-spacing: 6px;
    padding: 4px 0;
  }

  .event-info { position: absolute; top: 192px; left: 42px; font-size: 19px; line-height: 1.6; font-weight: 500; }
  .event-info .row { display: flex; }
  .event-info .label { width: 112px; flex: none; }
  .event-info .indent { padding-left: 112px; }

  .couple-illustration {
    position: absolute; top: 196px; left: 600px; width: 215px; height: 158px;
    background: linear-gradient(180deg, var(--tint), var(--soft)); border-radius: 8px;
  }

  .contact-band { position: absolute; top: 362px; left: 28px; width: 791px; height: 128px; display: flex; }
  .contact-badge {
    width: 104px; background: var(--band); color: var(--paper);
    font-size: 22px; font-weight: 700; line-height: 1.35;
    display: flex; align-items: center; justify-content: center; text-align: center;
  }
  .contact-lines { flex: 1; padding-left: 14px; display: flex; flex-direction: column; justify-content: space-between; }
  .contact-row { display: flex; align-items: center; gap: 14px; }
  .channel {
    width: 62px; height: 62px; border-radius: 50%; background: var(--band); color: var(--paper);
    font-size: 16px; font-weight: 900; display: flex; align-items: center; justify-content: center; flex: none;
  }
  .channel.fax { width: 70px; height: 40px; border-radius: 20px; }
  .contact-value { font-size: 30px; font-weight: 900; letter-spacing: 0.5px; white-space: nowrap; }
  .contact-value.fax-number { font-size: 40px; }
  .mail-note { font-size: 11px; line-height: 1.3; color: var(--mid); margin-top: 2px; }

  .entry-form { position: absolute; top: 502px; left: 28px; width: 791px; border: 2px solid var(--ink); }
  .entry-form .form-bar { background: var(--band); color: var(--paper); font-size: 18px; font-weight: 700; padding: 3px 0 3px 220px; }
  .entry-form table { width: 100%; border-collapse: collapse; font-size: 16px; table-layout: fixed; }
  .entry-form th, .entry-form td { border: 1px solid var(--mid); height: 34px; padding: 0 10px; text-align: left; font-weight: 500; white-space: nowrap; }
  .entry-form th { background: var(--tint); }
  .entry-form .col-label { width: 140px; }
  .entry-form .col-value { width: 340px; }
  .entry-form .col-label2 { width: 110px; }
  .entry-form .pr-cell { height: 76px; vertical-align: top; padding-top: 4px; }
  .entry-form .date-cell span { display: inline-block; width: 70px; text-align: right; }

  .inquiry-box { position: absolute; top: 732px; left: 28px; width: 791px; height: 150px; border: 2px solid var(--ink); }
  .inquiry-box .inquiry-title { background: var(--tint); border-bottom: 1px solid var(--mid); font-size: 15px; font-weight: 700; padding: 3px 10px; }

  .notes { position: absolute; top: 900px; left: 42px; width: 770px; font-size: 15px; line-height: 1.6; list-style: none; }
  .notes li { padding-left: 1.3em; text-indent: -1.3em; }
  .notes .follow-up { margin-top: 2px; }

  .divider { position: absolute; top: 1038px; left: 28px; width: 791px; border-top: 2px solid var(--ink); }

  .office-name { position: absolute; top: 1056px; left: 42px; font-size: 38px; font-weight: 900; letter-spacing: 1px; }
  .office-phones { position: absolute; top: 1056px; left: 612px; font-size: 20px; font-weight: 700; line-height: 1.4; }
  .office-address { position: absolute; top: 1122px; left: 42px; font-size: 11px; color: var(--mid); }
</style>
</head>
<body>
<main class="sheet">
  <h1 class="event-title"><span class="title-mark"></span>渚トーク星結び</h1>
  <h2 class="form-heading">参加申込用紙</h2>

  <section class="event-info">
    <div class="row"><span class="label">〈日　時〉</span><span>2015年7月3日(金)～2015年7月5日(日)</span></div>
    <div class="row"><span class="label">〈会　場〉</span><span>神津島　(募集人数) 15名 (先着順)</span></div>
    <div class="row"><span class="label">〈参加資格〉</span><span>20歳から35歳までの神津島外在住の独身女性</span></div>
    <div class="indent">お一人様参加・シングルマザー・結婚歴あり歓迎</div>
    <div class="row"><span class="label">〈参加料金〉</span><span>15,000円/1人 (交通費・宿泊費・食費込み)</span></div>
  </section>

  <div class="couple-illustration" role="img" aria-label="寄り添う新郎新婦のイラスト"></div>

  <section class="contact-band">
    <div class="contact-badge">お申込は<br>こちら</div>
    <div class="contact-lines">
      <div>
        <div class="contact-row"><span class="channel">MAIL</span><span class="contact-value">shiomi@hx.nagisanet-example.jp</span></div>
        <p class="mail-note">メールでのお申し込みは①氏名②生年月日③住所④電話番号⑤メールアドレスを添えて上記のアドレスまでご送信ください。</p>
      </div>
      <div class="contact-row"><span class="channel fax">FAX</span><span class="contact-value fax-number">04992-7-5530</span></div>
    </div>
  </section>

  <section class="entry-form">
    <div class="form-bar">お申込みフォーム</div>
    <table>
      <colgroup><col class="col-label"><col class="col-value"><col class="col-label2"><col></colgroup>
      <tr><th>氏　名</th><td></td><th>(ふりがな)</th><td></td></tr>
      <tr><th>生年月日</th><td class="date-cell"><span>年</span><span>月</span><span>日</span></td><th>電話番号</th><td></td></tr>
      <tr><th>メールアドレス</th><td colspan="3"></td></tr>
      <tr><th class="pr-cell">自己PR</th><td colspan="3" class="pr-cell"></td></tr>
    </table>
  </section>

  <section class="inquiry-box">
    <div class="inquiry-title">お問合わせ・お申込み</div>
  </section>

  <ol class="notes">
    <li>1. 申し込み・キャンセルは6月7日(日)までにお願いします。</li>
    <li>2. 男女比は出来る限り調整しますが同数にならないこともありますのでご了承願います。</li>
    <li>3. 個人情報は厳重に管理し、本事業のみの使用とさせていただきます。</li>
    <li>4. 悪天候時はプログラム内容を変更または中止する場合があります。</li>
    <li class="follow-up">※申し込み受付後、事務局より順次詳細をお送りいたします。</li>
  </ol>

  <div class="divider"></div>

  <footer>
    <p class="office-name">汐見村商工会青年部事務局</p>
    <p class="office-phones">TEL 04992-7-4418<br>FAX 04992-7-5530</p>
    <p class="office-address">〒100-0999 東京都汐見村汐見村2483番地　TEL 04992-7-4418　FAX 04992-7-5530　MAIL shiomi@hx.nagisanet-example.jp</p>
  </footer>
</main>
</body>
</html>
```